Psychiatric Office Needs a Website- 1st Time Ever!

Been in practice since 2003 with no website, but finally ready to dive in. We are Maplecrest Behavioral Healthcare, a mental health outpatient practice based in Fayetteville, Georgia that sees diverse individuals and families from childhood to advanced age for a variety of conditions. We've grown by word of mouth and referral but would now like to have a digital footprint. Be the pioneer of our website and we will be sure to share. We would like to see designs that are modern, animated, fairly colorful, easy to read, and caters to all ages. Also, we would like the design to take the whole page (not be centered) and can be viewed well on phone/tablet. Please see our outline for more information. Our motto/slogan is: Maplecrest Behavioral Healthcare- A step forward in your wellness journey, so the design should try to reflect that.
Updates

Target Market(s)

Children through elderly

Industry/Entity Type

Medical

Logo Text

Stepping forward in your wellness journey

Number of Pages Required

1 page

Colors

Designer to choose colors to be used in the design.

Requirements
Must have
• Animation or moving pictures.
• Color.
• Concise.
• User friendly
• Diversity in the stock photos

```html
<!DOCTYPE html>
<html lang="en">
<head>
<meta charset="utf-8">
<title>Maplecrest Behavioral Healthcare</title>
<link href="https://fonts.googleapis.com/css2?family=Roboto:ital,wght@0,300;0,400;0,500;0,700;1,400&display=swap" rel="stylesheet">
<style>
:root{
  --blue:#4f7fd9;
  --blue-dark:#3a63c2;
  --teal:#41c2c9;
  --ink:#222;
  --text:#555;
  --muted:#888;
  --line:#e5e5e5;
  --footer-bg:#f4f5f7;
  --white:#fff;
}
*{box-sizing:border-box;margin:0;padding:0}
html,body{width:1200px;height:3056px;overflow:hidden}
body{font-family:"Roboto",Arial,sans-serif;color:var(--text);background:var(--white);position:relative}
.abs{position:absolute}
.topbar{position:absolute;top:0;left:0;width:1200px;height:75px;border-bottom:1px solid var(--line)}
.brand{position:absolute;left:80px;top:16px;display:flex;align-items:center;gap:12px}
.brand-dot{width:36px;height:36px;border-radius:50%;background:var(--blue)}
.brand-name{font-size:19px;font-weight:500;color:var(--blue);line-height:1.1}
.brand-tag{font-size:12px;color:var(--muted);letter-spacing:.3px}
.contact-item{position:absolute;top:18px;display:flex;gap:12px;align-items:center;font-size:12px;color:var(--ink);line-height:1.5}
.contact-item b{font-weight:500}
.contact-item span{color:var(--muted)}
.nav{position:absolute;top:75px;left:0;width:1200px;height:45px}
.nav a{position:absolute;top:15px;font-size:12.5px;color:var(--ink);text-decoration:none}
.hero{position:absolute;top:120px;left:0;width:1200px;height:426px;background:linear-gradient(100deg,#5a7bd7 0%,#4a97d6 45%,#41c2c9 100%)}
.hero h1{position:absolute;left:80px;top:112px;font-size:26px;font-weight:700;color:var(--white)}
.hero p{position:absolute;left:80px;top:155px;width:430px;font-size:12.5px;line-height:1.75;color:var(--white)}
.btn-outline{position:absolute;font-size:11px;font-weight:500;letter-spacing:.5px;padding:9px 16px;border:1px solid currentColor;text-transform:uppercase}
.hero .btn-outline{left:80px;top:245px;color:var(--white)}
.hero-photo{position:absolute;right:0;top:0;width:560px;height:426px;background:linear-gradient(90deg,rgba(255,255,255,0),rgba(220,235,245,.35))}
.booking{position:absolute;left:764px;top:30px;width:296px;height:362px;background:rgba(30,60,110,.55);padding:22px 34px}
.booking h3{color:var(--white);font-size:15px;font-weight:700;margin-bottom:14px}
.field{height:34px;background:var(--white);margin-bottom:22px;border-radius:2px;font-size:10.5px;color:#aaa;padding:11px 12px;display:flex;justify-content:space-between}
.booking .submit{display:inline-block;background:var(--teal);color:var(--white);font-size:12px;font-weight:500;padding:10px 20px;border-radius:2px}
.slide-arrow{position:absolute;top:490px;width:30px;height:60px;background:var(--white);display:flex;align-items:center;justify-content:center}
.section-title{position:absolute;left:0;width:1200px;text-align:center;font-size:26px;font-weight:700;color:var(--ink)}
.section-title::after{content:"";display:block;width:44px;height:3px;background:var(--blue);margin:16px auto 0}
.vision{position:absolute;top:546px;left:0;width:1200px;height:548px;background:#fbfbfc}
.doctor-photo{position:absolute;left:120px;top:120px;width:250px;height:428px;background:linear-gradient(180deg,#e8edf2,#cfd8e2);border-radius:110px 110px 0 0}
.vm{position:absolute;left:433px;width:680px}
.vm h4{font-size:18px;font-weight:700;color:var(--ink);margin-bottom:12px}
.vm li{list-style:none;position:relative;padding-left:24px;font-size:12px;line-height:1.9;color:var(--text);margin-bottom:6px}
.vm li::before{content:"";position:absolute;left:0;top:5px;width:13px;height:13px;border-radius:50%;background:var(--blue)}
.vm li::after{content:"";position:absolute;left:4px;top:9px;width:3px;height:3px;border-top:1.5px solid #fff;border-right:1.5px solid #fff;transform:rotate(45deg)}
.services{position:absolute;top:1094px;left:0;width:1200px;height:609px}
.service{position:absolute;width:320px;padding-left:88px}
.service svg{position:absolute;left:0;top:0}
.service h5{font-size:14px;font-weight:500;color:var(--ink);line-height:1.4;margin-bottom:8px}
.service p{font-size:12.5px;line-height:1.75;color:var(--text)}
.testimonials{position:absolute;top:1703px;left:0;width:1200px;height:334px;background:linear-gradient(180deg,#5a7bd7,#41c2c9)}
.testimonials .section-title{color:var(--white);top:62px}
.testimonials .section-title::after{background:var(--white)}
.quote{position:absolute;left:180px;top:150px;width:840px;text-align:center;font-size:13px;font-style:italic;line-height:1.9;color:#eef4fb}
.quote-mark{position:absolute;left:-18px;top:-24px;font-size:60px;color:rgba(255,255,255,.35);font-style:normal}
.quote-by{position:absolute;left:0;width:1200px;top:246px;text-align:center;font-size:11.5px;font-weight:700;color:var(--white)}
.quote-role{position:absolute;left:0;width:1200px;top:265px;text-align:center;font-size:11.5px;color:#e6f0fa}
.news{position:absolute;top:2037px;left:0;width:1200px;height:678px}
.card{position:absolute;top:159px;width:330px}
.card-photo{height:234px;background:linear-gradient(135deg,#dfe9f3,#b9cde0)}
.card h3{font-size:18px;font-weight:500;color:var(--ink);margin-top:32px;text-transform:uppercase}
.card time{display:block;font-size:10.5px;color:var(--blue);margin:6px 0 8px}
.card p{font-size:12px;line-height:1.8;color:var(--text);height:112px;overflow:hidden}
.card .btn-outline{position:static;display:inline-block;color:var(--ink);border-color:#aaa;font-size:10px;padding:7px 12px;margin-top:14px}
.footer{position:absolute;top:2715px;left:0;width:1200px;height:341px;background:var(--footer-bg)}
.footer h6{font-size:14px;font-weight:700;color:var(--ink);margin-bottom:18px}
.f-about{position:absolute;left:80px;top:40px;width:300px}
.f-about .brand-dot{width:40px;height:40px;border-radius:50%;background:var(--blue);margin-bottom:14px}
.f-about .brand-name{font-size:18px;margin-bottom:6px}
.f-about p{font-size:11px;line-height:1.8;color:var(--text)}
.copyright{position:absolute;left:80px;top:290px;font-size:11px;color:var(--ink)}
.f-links{position:absolute;left:434px;top:56px}
.f-links li{list-style:none;font-size:11.5px;color:var(--text);line-height:26.5px}
.f-links li::before{content:"› ";color:var(--muted)}
.f-events{position:absolute;left:613px;top:56px;width:250px}
.event{display:flex;gap:12px;margin-bottom:16px}
.event-thumb{width:42px;height:42px;background:linear-gradient(135deg,#d9c4b3,#9fb5cc);flex:none}
.event b{display:block;font-size:11.5px;font-weight:500;color:var(--ink);margin-bottom:4px}
.event span{display:block;font-size:9.5px;font-style:italic;color:var(--muted);line-height:1.4}
.f-contact{position:absolute;left:880px;top:56px}
.f-contact li{list-style:none;display:flex;gap:10px;align-items:center;font-size:11.5px;color:var(--ink);margin-bottom:16px}
.socials{display:flex;gap:6px;margin-top:8px}
.socials i{width:26px;height:26px;border-radius:50%;background:var(--blue);display:block}
</style>
</head>
<body>

<header class="topbar">
  <div class="brand">
    <div class="brand-dot"></div>
    <div>
      <div class="brand-name">Maplecrest Behavioral Healthcare</div>
      <div class="brand-tag">Your Steady Path to Everyday Wellness</div>
    </div>
  </div>
  <div class="contact-item" style="left:488px">
    <svg width="26" height="26" viewBox="0 0 24 24"><path d="M6.6 10.8a15 15 0 0 0 6.6 6.6l2.2-2.2c.3-.3.7-.4 1-.2 1.1.4 2.3.6 3.6.6.6 0 1 .4 1 1V20c0 .6-.4 1-1 1A17 17 0 0 1 3 4c0-.6.4-1 1-1h3.5c.6 0 1 .4 1 1 0 1.3.2 2.5.6 3.6.1.3 0 .7-.2 1z" fill="var(--blue)"/></svg>
    <div><b>+(770) 555 - 0142</b><br><span>+(770) 555 - 0143</span></div>
  </div>
  <div class="contact-item" style="left:683px">
    <svg width="26" height="26" viewBox="0 0 24 24"><circle cx="12" cy="12" r="11" fill="var(--blue)"/><path d="M12 6v6l4 2" stroke="#fff" stroke-width="2" fill="none"/></svg>
    <div><b>Mon - Sat: 8:30 AM - 6:30PM</b><br><span>Sun: 9:00 AM - 12:30PM</span></div>
  </div>
  <div class="contact-item" style="left:940px">
    <svg width="28" height="22" viewBox="0 0 28 22"><rect width="28" height="22" rx="2" fill="var(--blue)"/><path d="M2 3l12 9 12-9" stroke="#fff" stroke-width="2" fill="none"/></svg>
    <div><b>office@maplecrest-care.com</b><br><span>info@maplecrest-care.com</span></div>
  </div>
</header>

<nav class="nav">
  <a style="left:101px">Home</a>
  <a style="left:159px">About Us</a>
  <a style="left:238px">Services</a>
  <a style="left:310px">Condition We Treat</a>
  <a style="left:452px">New Patients</a>
  <a style="left:552px">Contact Us</a>
  <svg class="abs" style="left:1060px;top:14px" width="18" height="18" viewBox="0 0 18 18"><circle cx="7.5" cy="7.5" r="5.5" stroke="#222" stroke-width="2" fill="none"/><path d="M12 12l5 5" stroke="#222" stroke-width="2"/></svg>
  <svg class="abs" style="left:1104px;top:15px" width="16" height="14" viewBox="0 0 16 14"><path d="M0 1h16M0 7h16M0 13h16" stroke="#222" stroke-width="2"/></svg>
</nav>

<section class="hero">
  <div class="hero-photo" role="img" aria-label="Photo of a smiling doctor in a bright clinic"></div>
  <h1>NULLAM SCELERISQUE</h1>
  <p>Lorem ipsum dolor sit amet, consectetur adipiscing elit. Curabitur et lacus hendrerit, dignissim dui quis, porta lacus. Aenean mattis sem iaculis, posuere quam finibus, posuere lectus.</p>
  <span class="btn-outline">Read More</span>
  <form class="booking">
    <h3>BOOK APPOINTMENT</h3>
    <div class="field">Full Name <span>●</span></div>
    <div class="field">Phone <span>✆</span></div>
    <div class="field">mm / dd / yyyy <span>▦</span></div>
    <div class="field">Choose Department <span>⌄</span></div>
    <span class="submit">Submit Now</span>
  </form>
</section>
<div class="slide-arrow" style="left:0;border-radius:0 30px 30px 0"><svg width="10" height="12"><path d="M8 1L3 6l5 5" stroke="#333" stroke-width="2" fill="none"/></svg></div>
<div class="slide-arrow" style="right:0;border-radius:30px 0 0 30px"><svg width="10" height="12"><path d="M2 1l5 5-5 5" stroke="#333" stroke-width="2" fill="none"/></svg></div>

<section class="vision">
  <h2 class="section-title" style="top:46px">VISION &amp; MISSION</h2>
  <div class="doctor-photo" role="img" aria-label="Photo of a senior doctor holding a clipboard"></div>
  <div class="vm" style="top:130px">
    <h4>VISION</h4>
    <ul><li>To be the leading provider of outpatient psychiatric care in the Maplecrest Valley area, working together to promote (the) mental wellness of our community</li></ul>
    <h4 style="margin-top:18px">MISSION</h4>
    <ul>
      <li>To provide mental health services to children, adults, and the developmentally disabled population that is culturally sensitive regardless of age, race, gender, orientation, religion, or creed;</li>
      <li>To work hand in hand with clients to overcome mental health challenges and improve their quality of life;</li>
      <li>To partner with families and caregivers in achieving desired treatment goals for the client;</li>
      <li>To provide compassionate care within an environment that fosters healing and recovery;</li>
      <li>To bring hope and strengthen faith.</li>
      <li>We aim to offer service that patients recommend to family and friends, that other providers prefer, and is relevant in the community we serve.</li>
    </ul>
  </div>
</section>

<section class="services">
  <h2 class="section-title" style="top:56px">OUR SERVICES</h2>

  <div class="service" style="left:80px;top:160px">
    <svg width="62" height="62" viewBox="0 0 62 62"><path d="M10 6v18a12 12 0 0 0 24 0V6" stroke="#37a8c4" stroke-width="4" fill="none"/><path d="M22 36v8a12 12 0 0 0 24 0v-6" stroke="#37a8c4" stroke-width="4" fill="none"/><circle cx="46" cy="32" r="6" fill="var(--blue)"/></svg>
    <h5>Diagnostic Evaluation &amp; Treatment</h5>
    <p>Lorem ipsum dolor sit amet, cons ectetuer. Proin gravida nibh vel velit auctor aliquet. Aenean sollicitudi</p>
  </div>
  <div class="service" style="left:444px;top:160px">
    <svg width="62" height="62" viewBox="0 0 62 62"><circle cx="30" cy="30" r="24" fill="#37a8c4"/><path d="M20 26c4-6 14-6 20 0M22 36c6 4 12 4 18 0" stroke="#fff" stroke-width="3" fill="none"/></svg>
    <h5>Psychopharmacology</h5>
    <p>Lorem ipsum dolor sit amet, cons ectetuer. Proin gravida nibh vel velit auctor aliquet. Aenean sollicitudi</p>
  </div>
  <div class="service" style="left:808px;top:160px">
    <svg width="62" height="62" viewBox="0 0 62 62"><path d="M28 4v14c-14 4-16 26 2 30 12 2 18-10 12-20-4-6-6-6-6-10V4z" fill="#37a8c4"/></svg>
    <h5>Bariatric Pre-Surgical Consultation (and other surgeries)</h5>
    <p>Lorem ipsum dolor sit amet, cons ectetuer. Proin gravida nibh vel velit auctor aliquet. Aenean sollicitudi</p>
  </div>

  <div class="service" style="left:80px;top:304px">
    <svg width="62" height="62" viewBox="0 0 62 62"><circle cx="22" cy="8" r="5" fill="var(--blue)"/><path d="M22 16v18h16l6 14" stroke="#37a8c4" stroke-width="4" fill="none"/><circle cx="24" cy="42" r="13" stroke="#37a8c4" stroke-width="4" fill="none"/></svg>
    <h5>Disability and Work-Related Reports (Include?)</h5>
    <p>Lorem ipsum dolor sit amet, cons ectetuer. Proin gravida nibh vel velit auctor aliquet. Aenean sollicitudi</p>
  </div>
  <div class="service" style="left:444px;top:304px">
    <svg width="62" height="62" viewBox="0 0 62 62"><circle cx="30" cy="12" r="9" fill="#37a8c4"/><rect x="18" y="24" width="24" height="20" rx="8" fill="var(--blue)"/><rect x="16" y="46" width="10" height="12" rx="4" fill="#37a8c4"/><rect x="34" y="46" width="10" height="12" rx="4" fill="#37a8c4"/></svg>
    <h5>Early Childhood Assessments</h5>
    <p>Lorem ipsum dolor sit amet, cons ectetuer. Proin gravida nibh vel velit auctor aliquet. Aenean sollicitudi</p>
  </div>
  <div class="service" style="left:808px;top:304px">
    <svg width="62" height="62" viewBox="0 0 62 62"><path d="M30 8l22 22-6 6-22-22z" fill="#37a8c4"/><path d="M12 40l10-10 10 10-10 10z" fill="var(--blue)"/><circle cx="44" cy="48" r="7" stroke="#37a8c4" stroke-width="3" fill="none"/></svg>
    <h5>Substance Abuse Assessments</h5>
    <p>Lorem ipsum dolor sit amet, cons ectetuer. Proin gravida nibh vel velit auctor aliquet. Aenean sollicitudi</p>
  </div>

  <div class="service" style="left:80px;top:456px">
    <svg width="62" height="62" viewBox="0 0 62 62"><circle cx="20" cy="8" r="6" fill="var(--blue)"/><rect x="12" y="16" width="16" height="22" rx="4" fill="#37a8c4"/><rect x="13" y="38" width="6" height="22" fill="#37a8c4"/><rect x="21" y="38" width="6" height="22" fill="#37a8c4"/></svg>
    <h5>Developmental Disabilities</h5>
    <p>Lorem ipsum dolor sit amet, cons ectetuer. Proin gravida nibh vel velit auctor aliquet. Aenean sollicitudi</p>
  </div>
</section>

<section class="testimonials">
  <h2 class="section-title">WHAT PATIENTS ARE SAYING</h2>
  <blockquote class="quote"><span class="quote-mark">“</span>Lorem ipsum dolor sit amet, consectetur adipiscing elit. Cras vitae sagittis lectus. Aliquam erat volutpat. Etiam eu suscipit lorem. Ut eget massa venenatis, pellentesque nibh et, fermentum odio. Sed in cursus uma. Quisque eu mi tortor. Pellentesque cursus turpis tellus, semper vehicula justo ornare vel. Fusce imperdiet interdum felis.</blockquote>
  <div class="quote-by">EUISMOD LACUS</div>
  <div class="quote-role">Cras orci nisl</div>
</section>

<section class="news">
  <h2 class="section-title" style="top:60px">LATEST NEWS</h2>
  <article class="card" style="left:80px">
    <div class="card-photo" role="img" aria-label="Photo of two medical staff reviewing a tablet"></div>
    <h3>Vivamus est velit</h3>
    <time>21/09/2017</time>
    <p>Lorem ipsum dolor sit amet, consectetur adipiscing elit. Curabitur et lacus hendrerit, dignissim dui quis, porta lacus. Aenean mattis sem iaculis, posuere quam finibus, posuere lectus. Mauris accumsan purus neque, lacinia gravida ante viverra eget.</p>
    <span class="btn-outline">Read More</span>
  </article>
  <article class="card" style="left:434px">
    <div class="card-photo" role="img" aria-label="Photo of a doctor greeting an elderly patient"></div>
    <h3>Quisque non mauris venenatis</h3>
    <time>21/09/2017</time>
    <p>Vivamus ornare sollicitudin nibh ac laoreet. Donec feugiat elementum volutpat. Morbi facilisis auctor ex, ut ultricies sapien consectetur accumsan. Cras molestie at augue ac finibus. Cras vehicula diam nec neque ullamcorper, sit amet viverra quam molestie.</p>
    <span class="btn-outline">Read More</span>
  </article>
  <article class="card" style="left:790px">
    <div class="card-photo" role="img" aria-label="Photo of a doctor with a mother and young child"></div>
    <h3>Aliquam feugiat commodo</h3>
    <time>21/09/2017</time>
    <p>Nullam porta dapibus tincidunt. Aenean tincidunt nisi vel tellus placerat lacinia. Aliquam fringilla luctus risus, ac mollis odio rutrum et. Donec vitae urna in odio tincidunt pellentesque nec ac ex. Etiam ornare cursus nulla, quis tincidunt est mollis blandit.</p>
    <span class="btn-outline">Read More</span>
  </article>
</section>

<footer class="footer">
  <div class="f-about">
    <div class="brand-dot"></div>
    <div class="brand-name">Maplecrest Behavioral Healthcare</div>
    <div class="brand-tag" style="margin-bottom:14px">Your Steady Path to Everyday Wellness</div>
    <p>Quisque quis lacinia velit. Duis at tincidunt nisi. Vestibulum ante ipsum primis in faucibus orci luctus et ultrices posuere cubilia Curae; Nunc blandit sed magna nec rutrum. Vestibulum mollis quam nisi. Vivamus est velit, congue vitae massa eget, volutpat hendrerit tellus.</p>
  </div>
  <div class="copyright">Copyright © 2017 Maplecrest Behavioral Healthcare</div>

  <div class="f-links">
    <h6>LINKS</h6>
    <ul>
      <li>Cancellation Policy</li><li>Telephone Call Policy</li><li>Services</li><li>Refill Policy</li><li>Payment Policy</li><li>Accepted Insurances</li><li>Bio Philosophy</li><li>FAQ</li>
    </ul>
  </div>

  <div class="f-events">
    <h6>LATEST EVENTS</h6>
    <div class="event"><div class="event-thumb" role="img" aria-label="Event photo"></div><div><b>Aliquam Hendrerit Massa</b><span>Cras ol dignissim libero, sit amet elementum nunc.</span></div></div>
    <div class="event"><div class="event-thumb" role="img" aria-label="Event photo"></div><div><b>Duis Tortor Eros</b><span>Cras ol dignissim libero, sit amet elementum nunc.</span></div></div>
    <div class="event"><div class="event-thumb" role="img" aria-label="Event photo"></div><div><b>Ullamcorper Augue</b><span>Cras ol dignissim libero, sit amet elementum nunc.</span></div></div>
  </div>

  <div class="f-contact">
    <h6>CONTACT</h6>
    <ul>
      <li><svg width="13" height="13" viewBox="0 0 24 24"><path d="M6.6 10.8a15 15 0 0 0 6.6 6.6l2.2-2.2c.3-.3.7-.4 1-.2 1.1.4 2.3.6 3.6.6.6 0 1 .4 1 1V20c0 .6-.4 1-1 1A17 17 0 0 1 3 4c0-.6.4-1 1-1h3.5c.6 0 1 .4 1 1 0 1.3.2 2.5.6 3.6.1.3 0 .7-.2 1z" fill="#222"/></svg>(770) 555 - 0142</li>
      <li><svg width="13" height="11" viewBox="0 0 28 22"><rect width="28" height="22" rx="2" fill="#222"/><path d="M2 3l12 9 12-9" stroke="#fff" stroke-width="2" fill="none"/></svg>info@maplecrest-care.com</li>
      <li><svg width="12" height="15" viewBox="0 0 12 16"><path d="M6 0a6 6 0 0 0-6 6c0 4.5 6 10 6 10s6-5.5 6-10a6 6 0 0 0-6-6z" fill="#222"/><circle cx="6" cy="6" r="2" fill="#fff"/></svg>P.O. Box 418, Fayette Ridge Road.</li>
    </ul>
    <div class="socials"><i></i><i></i><i></i><i></i></div>
  </div>
</footer>

</body>
</html>
```